Poster for List of Company Values

We need a poster to outline our Values which will be displayed in our office as well as posted on our website and other platforms (so need to allow for some flexibly in its application).

File attached outlines what we currently have with design and also our company style guide.

Note that we are looking for a modern, clean look, which still represents our core activities of construction and environmental services.

You can also reference our website here:

https://quorvelgroup.com.au/

Happy to answer any questions you might have.

Thanks for your interest,
Brent

Target Market(s)

Internal and External clients

Industry/Entity Type

Construction, water and recycling

Font styles to use
Sans Serif

Requirements
Must have
• All values on the one page. Graphic to represent each value. Also needs to use company logo
Nice to have
• Preference for poster to be orientated in landscape
Should not have
• Do not follow example provided, this is only to demonstrate what we have to date and also the text required

```html
<!DOCTYPE html>
<html lang="en">
<head>
<meta charset="utf-8">
<title>List of Company Values – Quorvel Group</title>
<link rel="stylesheet" href="https://fonts.googleapis.com/css2?family=Bebas+Neue&family=Montserrat:wght@600;700&display=swap">
<style>
  :root {
    --brand-blue: #123c8c;
    --brand-navy: #0a0d86;
    --brand-green: #43ad48;
    --brand-charcoal: #343437;
    --paper: #ffffff;
    --ink: #2e2e30;
  }
  * { box-sizing: border-box; margin: 0; padding: 0; }
  html, body { width: 800px; height: 1200px; overflow: hidden; background: var(--paper); }
  .poster { position: relative; width: 800px; height: 1200px; background: var(--paper); overflow: hidden; font-family: "Montserrat", sans-serif; }

  .corner { position: absolute; top: 0; }
  .corner--left { left: 0; }
  .corner--right { right: 0; }

  .brand { position: absolute; top: 42px; left: 0; width: 800px; display: flex; justify-content: center; align-items: center; gap: 12px; }
  .brand__mark { width: 30px; height: 30px; background: var(--brand-green); }
  .brand__name { font-family: "Montserrat", sans-serif; font-weight: 600; color: var(--ink); font-size: 28px; line-height: 30px; }

  .title-row { position: absolute; top: 148px; left: 0; width: 800px; height: 56px; }
  .title-row__bar { position: absolute; top: 10px; height: 40px; }
  .title-row__bar--navy { left: 0; width: 140px; background: var(--brand-navy); }
  .title-row__bar--green { right: 0; width: 126px; background: var(--brand-green); }
  .title-row__text { position: absolute; left: 158px; width: 500px; text-align: center; font-family: "Bebas Neue", sans-serif; font-size: 64px; line-height: 60px; color: #111; letter-spacing: 0.5px; }

  .value { position: absolute; width: 280px; color: #fff; }
  .value--blue { background: var(--brand-blue); }
  .value--green { background: var(--brand-green); }
  .value--dark { background: var(--brand-charcoal); }
  .value__body { position: absolute; left: 86px; right: 10px; top: 0; bottom: 0; display: flex; flex-direction: column; justify-content: center; }
  .value__heading { font-family: "Bebas Neue", sans-serif; font-size: 56px; line-height: 50px; letter-spacing: 0.3px; }
  .value__text { margin-top: 14px; font-weight: 700; font-size: 14.5px; line-height: 19.5px; }

  .badge { position: absolute; width: 156px; height: 156px; margin: -78px 0 0 -78px; border-radius: 50%; border: 2px dotted var(--brand-green); background: var(--paper); }
  .badge__ring { position: absolute; inset: 8px; border-radius: 50%; background: var(--paper); box-shadow: 0 3px 8px rgba(0,0,0,0.25); }
  .badge__icon { position: absolute; inset: 18px; border-radius: 50%; }
  .badge--blue .badge__icon { background: var(--brand-blue); }
  .badge--green .badge__icon { background: var(--brand-green); }
  .badge--dark .badge__icon { background: var(--brand-charcoal); }

  .footer { position: absolute; left: 0; bottom: 0; width: 800px; height: 68px; }
  .footer__url { position: absolute; left: 0; width: 800px; bottom: 20px; text-align: center; color: #fff; font-family: "Montserrat", sans-serif; font-weight: 600; font-size: 22px; letter-spacing: 2.5px; }
</style>
</head>
<body>
<main class="poster">
  <svg class="corner corner--left" width="110" height="125" viewBox="0 0 110 125" aria-hidden="true">
    <polygon points="0,60 30,0 48,0 0,95" fill="var(--brand-green)"/>
    <polygon points="0,120 62,0 92,0 22,125 0,125" fill="var(--brand-green)"/>
  </svg>
  <svg class="corner corner--right" width="70" height="110" viewBox="0 0 70 110" aria-hidden="true">
    <polygon points="0,0 70,0 70,110" fill="var(--brand-blue)"/>
  </svg>

  <header class="brand">
    <span class="brand__mark" aria-hidden="true"></span>
    <p class="brand__name">QUORVEL<br>Group</p>
  </header>

  <div class="title-row">
    <span class="title-row__bar title-row__bar--navy"></span>
    <h1 class="title-row__text">List of Company Values</h1>
    <span class="title-row__bar title-row__bar--green"></span>
  </div>

  <section class="value value--blue" style="left:105px; top:232px; height:274px;">
    <div class="value__body">
      <h2 class="value__heading">Be Loyal</h2>
      <p class="value__text">We take care of our own and provide opportunities to listen and support each other.</p>
    </div>
  </section>
  <section class="value value--blue" style="left:486px; top:232px; height:274px;">
    <div class="value__body">
      <h2 class="value__heading">Show<br>Respect</h2>
      <p class="value__text">We value the diversity and opinions of all.</p>
    </div>
  </section>
  <section class="value value--green" style="left:105px; top:519px; height:275px;">
    <div class="value__body">
      <h2 class="value__heading">Show<br>Initiative</h2>
      <p class="value__text">We celebrate and recognize our own and encourage forward thinking.</p>
    </div>
  </section>
  <section class="value value--green" style="left:486px; top:519px; height:275px;">
    <div class="value__body">
      <h2 class="value__heading">Be Open<br>&amp; Honest</h2>
      <p class="value__text">We are clear and open with each other, and provide an approachable and friendly environment.</p>
    </div>
  </section>
  <section class="value value--dark" style="left:105px; top:809px; height:288px;">
    <div class="value__body">
      <h2 class="value__heading">Think<br>Team</h2>
      <p class="value__text">We communicate effectively and work as a team by helping and supporting each other.</p>
    </div>
  </section>
  <section class="value value--dark" style="left:486px; top:809px; height:288px;">
    <div class="value__body">
      <h2 class="value__heading">Be<br>Positive</h2>
      <p class="value__text">SMILE<br>We are solutions focused and encourage a positive attitude turning a negative into a positive.</p>
    </div>
  </section>

  <div class="badge badge--blue" style="left:105px; top:366px;"><span class="badge__ring"></span><span class="badge__icon" role="img" aria-label="Icon of open hands holding a person beneath three stars"></span></div>
  <div class="badge badge--blue" style="left:486px; top:366px;"><span class="badge__ring"></span><span class="badge__icon" role="img" aria-label="Icon of a handshake under a heart"></span></div>
  <div class="badge badge--green" style="left:105px; top:655px;"><span class="badge__ring"></span><span class="badge__icon" role="img" aria-label="Icon of a light bulb with a dollar sign and a rising bar chart"></span></div>
  <div class="badge badge--green" style="left:486px; top:655px;"><span class="badge__ring"></span><span class="badge__icon" role="img" aria-label="Icon of two hands holding a glowing heart"></span></div>
  <div class="badge badge--dark" style="left:105px; top:945px;"><span class="badge__ring"></span><span class="badge__icon" role="img" aria-label="Icon of a group of people as a team"></span></div>
  <div class="badge badge--dark" style="left:486px; top:945px;"><span class="badge__ring"></span><span class="badge__icon" role="img" aria-label="Icon of a thumbs-up hand in a circle"></span></div>

  <footer class="footer">
    <svg width="800" height="68" viewBox="0 0 800 68" aria-hidden="true">
      <polygon points="148,0 662,0 716,68 105,68" fill="var(--brand-charcoal)"/>
    </svg>
    <p class="footer__url">www.quorvelgroup.com.au</p>
  </footer>
</main>
</body>
</html>
```